Silver Hollow is a cabin in Gatlinburg, Tennessee, near the Pinecrest Ridge National Park. When our cabin was built, there was one thing more important than any other--peace. The front of our cabin is surrounded by woods. It has a huge deck with a swing, Adirondack chairs, and a love seat for relaxation. The back deck has a hot tub, a large round glass table for cocktails or dinner, and because we left no stone unturned, we have a telescope for stargazing. There are two master suites, each have a private bath with a large jetted tub, seperate shower, flat screen TV, and a door that leads to the back deck.

Contact Information for Business Card

Silver Hollow Vacation Rentals, LLC
817 Harlow Brook Ct.
Oakland, Ky 40000
Janet M. Colbert, Owner/Manager
(270) 555.0147

```html
<!DOCTYPE html>
<html lang="en">
<head>
<meta charset="utf-8">
<title>Silver Hollow Vacation Rentals – Business Card</title>
<link rel="stylesheet" href="https://fonts.googleapis.com/css2?family=Lato:wght@300;400;700;900&display=swap">
<style>
  :root {
    --brand-blue: #21418f;
    --paper: #ffffff;
    --circle-paper: #f3f3f3;
    --backdrop: #e9e9e9;
    --ink-light: #ffffff;
    --ink-soft: #dfe6f5;
  }
  * { margin: 0; padding: 0; box-sizing: border-box; }
  html, body {
    width: 1200px; height: 900px; overflow: hidden;
    background: var(--backdrop);
    font-family: "Lato", Arial, sans-serif;
  }
  .canvas { position: relative; width: 1200px; height: 900px; }

  .card {
    position: absolute;
    width: 500px; height: 286px;
    background: var(--paper);
    overflow: hidden;
    box-shadow: 0 8px 24px rgba(0,0,0,0.12);
  }
  .card-front { left: 70px; top: 307px; }
  .card-back  { left: 630px; top: 307px; }
  .card-art { position: absolute; inset: 0; }

  .holder { position: absolute; left: 42px; top: 34px; color: var(--ink-light); }
  .holder-name { font-size: 25px; font-weight: 700; letter-spacing: 0.3px; }
  .holder-title { font-size: 13px; font-weight: 300; margin-top: 2px; color: var(--ink-soft); }

  .contact {
    position: absolute; left: 42px; top: 112px;
    color: var(--ink-light); font-size: 13px; line-height: 1.28; font-weight: 400;
    list-style: none;
  }
  .contact-label { font-weight: 300; color: var(--ink-soft); }

  .wordmark {
    position: absolute; text-align: center;
    color: var(--brand-blue); font-weight: 900; line-height: 1.1;
    text-transform: uppercase;
  }
  .wordmark-name { display: block; font-size: 24px; letter-spacing: 1px; }
  .wordmark-line { display: block; font-size: 11px; letter-spacing: 0.6px; margin-top: 3px; }
  .card-front .wordmark { left: 270px; top: 192px; width: 230px; }
  .card-back .wordmark { left: 40px; top: 118px; width: 300px; }
  .card-back .wordmark-name { font-size: 27px; }
  .card-back .wordmark-line { font-size: 12px; }
</style>
</head>
<body>
<main class="canvas">

  <section class="card card-front" aria-label="Business card front">
    <svg class="card-art" width="500" height="286" viewBox="0 0 500 286" aria-hidden="true">
      <rect width="500" height="286" fill="var(--brand-blue)"/>
      <circle cx="388" cy="212" r="125" fill="var(--circle-paper)"/>
    </svg>
    <header class="holder">
      <h1 class="holder-name">Janet M. Colbert</h1>
      <p class="holder-title">Owner/Manager</p>
    </header>
    <ul class="contact">
      <li class="contact-label">telephone</li>
      <li>(270) 555.0147</li>
      <li class="contact-label">email</li>
      <li>info@silverhollowstay.com</li>
      <li class="contact-label">address</li>
      <li>817 Harlow Brook Ct.,</li>
      <li>Oakland, Ky 40000</li>
    </ul>
    <p class="wordmark">
      <span class="wordmark-name">Silver Hollow</span>
      <span class="wordmark-line">Vacation Rentals, LLC</span>
    </p>
  </section>

  <section class="card card-back" aria-label="Business card back">
    <svg class="card-art" width="500" height="286" viewBox="0 0 500 286" aria-hidden="true">
      <rect width="500" height="286" fill="var(--brand-blue)"/>
      <circle cx="190" cy="120" r="230" fill="var(--paper)"/>
    </svg>
    <p class="wordmark">
      <span class="wordmark-name">Silver Hollow</span>
      <span class="wordmark-line">Vacation Rentals, LLC</span>
    </p>
  </section>

</main>
</body>
</html>
```